Etikett für Honigunternehmen gesucht
Zielgruppe
Wir produzieren Honig, möchten aber in naher Zukunft auch andere Honigprodukte produzieren (Cremen, Wein, Likör......). Unsere Zielgruppe sind alle.
Aufgabenstellung
Wir wünschen uns Schlichtheit und Einfachheit. Wichtig ist uns auch, dass das Design modern wirkt. Es soll kein typisches Honigetikett mit 'Wiesen und Bienen' werden. Das Glas wird auch schlicht und modern werden. Es wird nur 250-g- und 500-g-Gläser geben. Die Gewichtsangabe muss sichtbar und mind. 4 mm groß sein. Name, Anschrift und Telefonnummer können auch am Deckel oder ganz klein und leserlich am unteren Etikettenrand stehen. Dabei ist zu beachten, dass der kleinste Buchstabe min. 1,2 mm groß ist.
Etiketten-Design für Honigglas Etiketten-Design für Honigglas"
Format: Etikett für 250-gr.-Honigglas (TO ∅ 63 mm). Standardmaßgrösse 165 × 40 mm Design: schlicht, hochwertig, modern, edel/royal, unkonventionelles Design (weg von Bienen, Waben, Landschaften usw.), dunkle Farbtöne in Kontrast zu heller Schrift, die beiden Textbausteine 'Los Nr. ' sowi..
Attraktives Etiketten-Design für Honig Attraktives Etiketten-Design für Honig"
Wir verkaufen zur Zeit vor allem Waldhonig, streben aber auch einen Blütenhonig an. Das Etikett soll daher entweder den Wald wiederspiegeln oder aber neutral sein, so dass der Schriftzug Waldhonig oder Blütenhonig jeweils eingesetzt werden kann. Wichtig ist mir der Ortszusatz 'aus dem Glottertal..
Etiketten-Design für Produkte eines Familienbetriebs mit Imkerei und Hühnerhaltung Etiketten-Design für Produkte eines Familienbetriebs mit Imkerei und Hühnerhaltung"
1. Zentrale, auf allen Etiketten wiederkehrende Elemente: - Unser Riegelhaus (stilisiert) (Bild beiliegend) - Das Wort 'Marlock' (Anmerkung: ohne Anführungszeichen) - die zentralen Elemente sollen die Produkte nicht überragen. 2. Dezente Adresse: - Familie Obrecht, Talbrunn, CH-9388 Forlenz 3...
Etiketten-Design für Kurkuma-Honig Etiketten-Design für Kurkuma-Honig"
Etikett für 500g // Stanze eckig (210x35mm), Druckdatei entsprechend Vorgaben https://etikettwerk-muster.de/faq/ Vorgaben für das Grünquell Logo im Anhang Vorgaben für EG Öko Logo : https://example-oekoamt.eu/landbau/bio/download/logo_de Pflichtangaben auf dem Etikett: Gewicht, Adresse siehe Beispiel..
Etiketten-Design für Blütenhonig und Waldhonig gesucht Etiketten-Design für Blütenhonig und Waldhonig gesucht"
Zwei verschiedene Etiketten-Desings 1 x Blütenhonig sowie 1 x Waldhonig für unterschiedliche Honigglasgrößen (500 g und 250 g) Die Maße für die Etiketten wären: Für 500-Gramm-Glas 210 mm x 45 mm für's 250-Gramm-Glas 180 mm x 38 mm. Wir sind auch offen für neue Vorschläge bezüglich ..

```html
<!DOCTYPE html>
<html lang="de">
<head>
<meta charset="utf-8">
<title>Brennwald Honig – Etikett 250g</title>
<link rel="stylesheet" href="https://fonts.googleapis.com/css2?family=Kalam:wght@400;700&display=swap">
<style>
  :root {
    --ink: #111111;
    --paper: #ffffff;
    --honey: #f5b819;
    --font-hand: "Kalam", cursive;
  }
  html, body {
    margin: 0;
    padding: 0;
    width: 1200px;
    height: 600px;
    overflow: hidden;
    background: var(--paper);
  }
  .label {
    position: relative;
    width: 1200px;
    height: 600px;
    background: var(--paper);
    color: var(--ink);
    font-family: var(--font-hand);
  }
  .weight {
    position: absolute;
    top: 16px;
    right: 22px;
    margin: 0;
    font-size: 48px;
    font-weight: 400;
    line-height: 1;
  }
  .brand {
    position: absolute;
    left: 0;
    top: 0;
    width: 100%;
    height: 100%;
    margin: 0;
    font-weight: 400;
  }
  .brand-name {
    position: absolute;
    left: 318px;
    top: 226px;
    font-size: 100px;
    line-height: 1;
    letter-spacing: -1px;
    white-space: nowrap;
  }
  .brand-product {
    position: absolute;
    left: 612px;
    top: 334px;
    font-size: 112px;
    line-height: 1;
    white-space: nowrap;
  }
  .brand-mark {
    position: absolute;
    left: 772px;
    top: 205px;
    width: 110px;
    height: 110px;
  }
  .imprint {
    position: absolute;
    left: 16px;
    right: 16px;
    bottom: 10px;
    margin: 0;
    display: flex;
    justify-content: space-between;
    align-items: baseline;
    font-size: 23px;
    font-style: normal;
    line-height: 1.2;
    white-space: nowrap;
  }
  .imprint .sep {
    font-weight: 700;
  }
</style>
</head>
<body>
  <main class="label">
    <p class="weight">250g</p>

    <h1 class="brand">
      <span class="brand-name">Brennwald</span>
      <span class="brand-product">Honig</span>
    </h1>

    <svg class="brand-mark" viewBox="0 0 110 110" role="img" aria-label="Illustration einer kleinen Biene">
      <circle cx="55" cy="55" r="50" fill="var(--honey)"/>
    </svg>

    <address class="imprint">
      <span class="imprint-name">Anton Brennwald</span>
      <span class="sep">·</span>
      <span class="imprint-street">Am Lindenhang 14</span>
      <span class="sep">·</span>
      <span class="imprint-town">4163 Kleinrodt</span>
      <span class="sep">·</span>
      <span class="imprint-phone">Tel.: +4366400012345</span>
      <span class="sep">·</span>
      <span class="imprint-country">Österreich</span>
    </address>
  </main>
</body>
</html>
```